International Biotech Startup needs a professionally looking web Design

We need a web design for a small biotech company based in Singapore which has global Pharma and Biotech Customers.

Our current website: www.zelvintralabs.com

However this was generated by few of us. We would require a professional design for biotech companies like us. The appearance of the website should be appealing to users and this is mainly a promotional website without any financial transactions.
Once the design is approved, we will provide the updated text.

Target Market(s)

Pharmaceutical, Biotech, healthcare

Industry/Entity Type

Biotechnology

Coding

Coded - Design and coding required

Number of Pages Required

5+ page

Requirements
Must have
• the website needs favicon.
Nice to have
• Please some of the companies websites that we like the most or they are in the similar domain. We would like to have something like that:
• http://www.pinecrestgenomics.com/
• http://www.marlowtherapeutics.com/
• http://www.tendrix.com/
• http://www.velunar.com/
• www.dornavil.com

```html
<!DOCTYPE html>
<html lang="en">
<head>
<meta charset="utf-8">
<title>Zelvintra Labs</title>
<link href="https://fonts.googleapis.com/css2?family=Open+Sans:wght@400;600;700&family=Raleway:wght@300;400;600&display=swap" rel="stylesheet">
<style>
:root{
  --navy:#24457a;
  --navy-deep:#17305c;
  --gold:#f2b51c;
  --ink:#4d5561;
  --muted:#8a929c;
  --band:#ededed;
  --line:#d9dde2;
  --white:#ffffff;
}
*{margin:0;padding:0;box-sizing:border-box}
html,body{width:1200px;height:2820px;overflow:hidden;background:var(--white)}
body{position:relative;font-family:"Open Sans",Arial,sans-serif;color:var(--ink)}
h1,h2,h3{font-weight:400}
.abs{position:absolute}

/* hero */
.hero-photo{left:0;top:0;width:1200px;height:600px;background:linear-gradient(100deg,#f4f7fa 0%,#e9eef3 40%,#dfe6ee 70%,#eef2f5 100%)}
.brand{left:0;top:150px;width:1200px;text-align:center;font-family:"Raleway",sans-serif;font-weight:600;font-size:92px;color:var(--navy);letter-spacing:2px}
.welcome{left:0;top:345px;width:1200px;text-align:center;font-family:"Raleway",sans-serif;font-weight:300;font-size:68px;letter-spacing:6px;color:var(--navy)}
.welcome-rule{top:388px;height:2px;background:var(--navy);width:230px}
.welcome-sub{left:0;top:460px;width:1200px;text-align:center;font-family:"Raleway",sans-serif;font-weight:400;font-size:56px;color:var(--navy)}
.welcome-sub span{color:var(--gold)}

/* nav */
.nav-shadow{left:0;top:648px;width:1200px;height:30px;background:linear-gradient(#d8dbe0,rgba(255,255,255,0))}
.nav-bar{left:0;top:644px;width:1200px;height:5px;background:var(--gold)}
.nav{left:190px;top:596px;display:flex}
.nav a{display:block;height:48px;line-height:48px;padding:0 22px;font-size:19px;color:var(--navy);text-decoration:none;border-right:1px solid var(--line);background:rgba(255,255,255,.85)}
.nav a.active{background:var(--navy);color:var(--white)}

/* about */
.about-title{left:75px;top:720px;font-family:"Raleway",sans-serif;font-size:46px;color:var(--navy)}
.about-rule{left:75px;top:785px;width:590px;height:2px;background:var(--line)}
.about-text{left:75px;top:808px;width:580px;font-size:13px;line-height:22px;color:var(--ink)}
.btn-more{left:75px;top:1040px;width:96px;height:50px;background:var(--gold);color:var(--white);font-size:14px;font-weight:600;text-align:center;line-height:50px}
.molecule{left:760px;top:720px;width:380px;height:290px;border-radius:20px;background:radial-gradient(ellipse at 55% 60%,#c9d3e0 0%,#e4e9f0 55%,#ffffff 80%)}

/* press band */
.press{left:75px;top:1150px;width:1050px;height:235px;background:var(--band)}
.press-shadow{left:75px;top:1385px;width:1050px;height:24px;background:linear-gradient(#d5d8dc,rgba(255,255,255,0))}
.badge{width:170px;height:40px;background:#cfd3d9;border-radius:4px}

/* features */
.feature-icon{width:150px;height:150px;border-radius:50%;background:var(--navy)}
.feature-title{width:500px;text-align:center;font-family:"Raleway",sans-serif;font-size:40px;color:var(--navy)}
.feature-text{width:420px;text-align:center;font-size:13px;line-height:22px;color:var(--ink)}
.divider{left:600px;top:1460px;width:1px;height:420px;background:var(--line)}

/* contact */
.contact-bg{left:0;top:1910px;width:1200px;height:610px;background:radial-gradient(circle at 30% 40%,#2f5a93 0%,#1d3f74 50%,#152f5a 100%)}
.contact-title{left:0;top:1935px;width:1200px;text-align:center;font-family:"Raleway",sans-serif;font-size:44px;color:var(--gold)}
.contact-rule{top:1968px;width:200px;height:2px;background:var(--gold)}
.contact-lede{left:300px;top:2010px;width:600px;text-align:center;font-size:12px;line-height:20px;color:#d7e0ec}
.sub-title{font-family:"Raleway",sans-serif;font-size:26px;color:var(--gold)}
.sub-rule{height:1px;background:rgba(242,181,28,.6)}
.field{top:2180px;height:40px;background:rgba(255,255,255,.12);border:1px solid rgba(255,255,255,.25);color:#dfe7f1;font-size:13px;padding:10px 12px}
.message{left:85px;top:2235px;width:695px;height:205px;background:rgba(255,255,255,.12);border:1px solid rgba(255,255,255,.25);color:#dfe7f1;font-size:13px;padding:10px 12px}
.send{left:150px;top:2370px;width:62px;height:62px;border-radius:50%;background:var(--navy-deep);border:3px solid #c9d3e0}
.info-disc{left:830px;top:2200px;width:270px;height:270px;border-radius:50%;background:var(--white)}
.info-text{left:850px;top:2330px;width:230px;text-align:center;font-size:12px;line-height:18px;color:var(--navy)}
.info-text strong{display:block;font-size:14px}

/* footer */
.top-btn{left:562px;top:2525px;width:76px;height:76px;border-radius:50%;border:3px solid var(--navy)}
.copy{left:0;top:2630px;width:1200px;text-align:center;font-size:14px;color:var(--muted)}
.social{top:2700px;width:44px;height:44px;border-radius:50%;background:#9ea5ae}
.foot-gold{left:0;top:2792px;width:1200px;height:20px;background:var(--gold)}
.foot-navy{left:0;top:2812px;width:1200px;height:8px;background:var(--navy)}
</style>
</head>
<body>

<header>
  <div class="abs hero-photo" role="img" aria-label="Soft-focus photo of a scientist in a laboratory examining a sample"></div>
  <div class="abs brand">Zelvintra Labs</div>
  <div class="abs welcome-rule" style="left:170px"></div>
  <div class="abs welcome-rule" style="left:800px"></div>
  <h1 class="abs welcome">WELCOME</h1>
  <h2 class="abs welcome-sub">To The <span>Zelvintra Labs</span></h2>

  <div class="abs nav-shadow"></div>
  <div class="abs nav-bar"></div>
  <nav class="abs nav">
    <a class="active">HOME</a><a>ABOUT</a><a>TECHNOLOGY</a><a>PRODUCTS</a><a>NEWS</a><a>CONTACTS</a>
  </nav>
</header>

<section class="about">
  <h2 class="abs about-title">About</h2>
  <div class="abs about-rule"></div>
  <p class="abs about-text">Zelvintra Labs is a Singapore based synthetic biology company. We specialise in providing customised membrane protein products, services and expertise for drug discovery, diagnostics and biomedical applications. Our company is backed by an international team of scientists with diverse interdisciplinary backgrounds in synthetic chemistry, materials science, nanotechnology, cell signalling and immunology. Our founders have extensive experience in biotechnology with a proven track record of working with small and big biotech and pharma companies all over the world.</p>
  <div class="abs btn-more">READ MORE</div>
  <div class="abs molecule" role="img" aria-label="Illustration of a molecular structure above an open capsule"></div>
</section>

<section class="press-band">
  <div class="abs press"></div>
  <div class="abs press-shadow"></div>
  <div class="abs badge" style="left:140px;top:1190px"></div>
  <div class="abs badge" style="left:390px;top:1190px"></div>
  <div class="abs badge" style="left:640px;top:1190px"></div>
  <div class="abs badge" style="left:890px;top:1190px"></div>
  <div class="abs badge" style="left:140px;top:1290px"></div>
  <div class="abs badge" style="left:390px;top:1290px"></div>
  <div class="abs badge" style="left:640px;top:1290px"></div>
  <div class="abs badge" style="left:890px;top:1290px"></div>
</section>

<section class="features">
  <div class="abs feature-icon" style="left:265px;top:1445px">
    <svg width="150" height="150" viewBox="0 0 150 150" fill="none" stroke="#fff" stroke-width="3">
      <ellipse cx="75" cy="75" rx="40" ry="15"/>
      <ellipse cx="75" cy="75" rx="40" ry="15" transform="rotate(60 75 75)"/>
      <ellipse cx="75" cy="75" rx="40" ry="15" transform="rotate(-60 75 75)"/>
      <circle cx="75" cy="75" r="5" fill="#fff"/>
    </svg>
  </div>
  <h3 class="abs feature-title" style="left:90px;top:1625px">Technology</h3>
  <p class="abs feature-text" style="left:130px;top:1690px">The artificial cell membrane Zelvintra is a proprietary technology which is used to provide high quality functional membrane proteins (drug targets, for example) in a native-like environment using engineered polymer membranes, without the use of cells.</p>

  <div class="abs divider"></div>

  <div class="abs feature-icon" style="left:785px;top:1445px">
    <svg width="150" height="150" viewBox="0 0 150 150" fill="none" stroke="#fff" stroke-width="3" stroke-linejoin="round">
      <path d="M45 60 L75 45 L105 60 L75 75 Z"/>
      <path d="M45 60 V95 L75 110 V75"/>
      <path d="M105 60 V95 L75 110"/>
    </svg>
  </div>
  <h3 class="abs feature-title" style="left:610px;top:1625px">Products</h3>
  <p class="abs feature-text" style="left:650px;top:1690px">In addition to partnering with our clients in key areas of drug discovery, Zelvintra Labs also provides high quality products per request for interested customers. Please let us know your needs via the Contact page, and our scientists will get back to you with more details.</p>
</section>

<section class="contact">
  <div class="abs contact-bg" role="img" aria-label="Deep blue background of magnified cells"></div>
  <div class="abs contact-rule" style="left:240px"></div>
  <div class="abs contact-rule" style="left:760px"></div>
  <h2 class="abs contact-title">Contact Us</h2>
  <p class="abs contact-lede">We work with pharma and biotech teams around the world. Send us a short note about your project and our scientists will reply soon with the details and next steps for working together.</p>

  <div class="abs sub-rule" style="left:85px;top:2148px;width:150px"></div>
  <div class="abs sub-rule" style="left:510px;top:2148px;width:270px"></div>
  <h3 class="abs sub-title" style="left:250px;top:2128px">Send Us a Message</h3>
  <h3 class="abs sub-title" style="left:880px;top:2128px">CONTACT INFO</h3>

  <div class="abs field" style="left:85px;width:205px">Name</div>
  <div class="abs field" style="left:305px;width:220px">E-Mail</div>
  <div class="abs field" style="left:540px;width:240px">Subject</div>
  <div class="abs message">Message</div>
  <div class="abs send">
    <svg width="56" height="56" viewBox="0 0 56 56" fill="none" stroke="#fff" stroke-width="2.5"><path d="M16 28 H38 M30 20 L38 28 L30 36"/></svg>
  </div>

  <div class="abs info-disc"></div>
  <svg class="abs" style="left:945px;top:2250px" width="40" height="56" viewBox="0 0 40 56">
    <path d="M20 2 C9 2 2 10 2 20 C2 34 20 54 20 54 C20 54 38 34 38 20 C38 10 31 2 20 2 Z" fill="#e0473c"/>
    <circle cx="20" cy="20" r="7" fill="#fff"/>
  </svg>
  <p class="abs info-text"><strong>Zelvintra Labs Pte Ltd.</strong>18 Kessel Way, Research Terrace Place, 4 Harlow Link 6, Singapore 000000</p>
</section>

<footer>
  <div class="abs top-btn">
    <svg width="70" height="70" viewBox="0 0 70 70" fill="none" stroke="#24457a" stroke-width="4"><path d="M22 42 L35 29 L48 42"/></svg>
  </div>
  <p class="abs copy">© Zelvintra Labs  2015. All Rights Reserved</p>
  <div class="abs social" style="left:502px"></div>
  <div class="abs social" style="left:556px"></div>
  <div class="abs social" style="left:610px"></div>
  <div class="abs social" style="left:664px"></div>
  <div class="abs foot-gold"></div>
  <div class="abs foot-navy"></div>
</footer>

</body>
</html>
```